General Contractors need a new Crisp updated Card Design

We need a new business card design for our company of 25 years based in Toronto call Holvaster Building Inc. : Our goal is to be the leading commercial contractors in Toronto by providing exceptional value to our clients. We work very hard to deliver professional, quality, service in conjunction with consistent price competitiveness to all of our clients on every single project.

Target Market(s)

Design & Build Clients

Industry/Entity Type

Construction Company

Contact Information for Business Card

Address:
18 North Tamlin Glen Road, Unit 57, Marbrook Vale, ON, K7T 2R9
Office: 905-218-5937

Holvasters Logo
Employee Job Description
Employee Cell Phone #
Employee Email
www.holvaster-example.com

Colors

Designer to choose colors to be used in the design.

Requirements
Must have
• Quote Company Saying:
• "Professional. Quality. Service."
Nice to have
• New Crisp up to date look. simple & fresh ( Not to Busy)
Should not have
• NO BLUE PRINTS ON THE BUSINESS CARDS

```html
<!DOCTYPE html>
<html lang="en">
<head>
<meta charset="utf-8">
<title>Holvaster Building Inc. – Business Card</title>
<link rel="stylesheet" href="https://fonts.googleapis.com/css2?family=Open+Sans:wght@400;600;700&display=swap">
<style>
  :root {
    --teal: #137f6e;
    --teal-soft: #a8cec5;
    --ink: #2c2c2c;
    --grey: #6d6d6d;
    --card: #ffffff;
    --backdrop: #2a2a2a;
  }
  * { box-sizing: border-box; margin: 0; padding: 0; }
  html, body {
    width: 1200px; height: 900px; overflow: hidden;
    background: var(--backdrop);
    font-family: "Open Sans", Arial, sans-serif;
  }
  .canvas {
    width: 1200px; height: 900px;
    display: flex; flex-direction: column; align-items: center; justify-content: center;
    gap: 40px;
  }
  .card {
    width: 665px; height: 380px;
    background: var(--card);
    position: relative;
    box-shadow: 0 6px 18px rgba(0,0,0,.45);
  }

  /* Front */
  .card-front {
    display: flex; flex-direction: column; align-items: center; justify-content: center;
  }
  .brand {
    display: flex; align-items: center; gap: 14px;
  }
  .brand-square {
    width: 34px; height: 34px; background: var(--teal); flex: none;
  }
  .brand-name {
    color: var(--teal); font-weight: 700; letter-spacing: .5px;
    text-transform: uppercase; line-height: 1.1;
  }
  .card-front .brand-name { font-size: 30px; }
  .tagline {
    margin-top: 34px;
    font-size: 15px; color: var(--grey); letter-spacing: .2px;
  }

  /* Back */
  .person {
    position: absolute; right: 44px; top: 34px; text-align: right;
  }
  .person-name {
    font-size: 18px; font-weight: 700; color: var(--teal); letter-spacing: .3px;
  }
  .person-role {
    font-size: 12px; font-weight: 600; color: var(--ink); margin-top: 1px;
  }
  .rule-top {
    position: absolute; left: 250px; right: 44px; top: 92px;
    height: 2px; background: var(--teal);
  }
  .card-back .brand {
    position: absolute; left: 40px; top: 122px;
  }
  .card-back .brand-name { font-size: 22px; }
  .rule-bottom {
    position: absolute; left: 40px; right: 44px; top: 178px;
    height: 2px; background: var(--teal);
  }
  .contacts {
    position: absolute; left: 40px; right: 44px; top: 208px;
    display: grid; grid-template-columns: 1.2fr 1fr 1fr; gap: 20px;
  }
  .contact {
    display: flex; flex-direction: column; align-items: center; text-align: center;
  }
  .contact-icon {
    width: 30px; height: 30px; border-radius: 50%;
    background: var(--teal);
    display: flex; align-items: center; justify-content: center;
    margin-bottom: 14px;
  }
  .contact-icon.soft { background: var(--teal-soft); }
  .contact-icon svg { width: 14px; height: 14px; }
  .contact-text {
    font-size: 13.5px; line-height: 1.35; color: var(--grey); font-style: normal;
  }
</style>
</head>
<body>
<main class="canvas">

  <section class="card card-front" aria-label="Card front">
    <div class="brand">
      <span class="brand-square" aria-hidden="true"></span>
      <span class="brand-name">Holvaster Building Inc.</span>
    </div>
    <p class="tagline">Professional. Quality. Service.</p>
  </section>

  <section class="card card-back" aria-label="Card back">
    <div class="person">
      <p class="person-name">MARLO TESSING</p>
      <p class="person-role">PRESIDENT</p>
    </div>
    <div class="rule-top"></div>

    <div class="brand">
      <span class="brand-square" aria-hidden="true"></span>
      <span class="brand-name">Holvaster Building Inc.</span>
    </div>
    <div class="rule-bottom"></div>

    <div class="contacts">
      <div class="contact">
        <span class="contact-icon" aria-hidden="true">
          <svg viewBox="0 0 14 14"><path d="M7 1a4 4 0 0 0-4 4c0 3 4 8 4 8s4-5 4-8a4 4 0 0 0-4-4z" fill="#fff"/><circle cx="7" cy="5" r="1.5" fill="var(--teal)"/></svg>
        </span>
        <address class="contact-text">18 North Tamlin Glen Road<br>Unit 57, Marbrook Vale, ON<br>K7T 2R9</address>
      </div>
      <div class="contact">
        <span class="contact-icon soft" aria-hidden="true">
          <svg viewBox="0 0 14 14"><rect x="4" y="1" width="6" height="12" rx="1" fill="#fff"/><rect x="5" y="3" width="4" height="7" fill="var(--teal-soft)"/></svg>
        </span>
        <p class="contact-text">905-218-5937<br>905-218-6041</p>
      </div>
      <div class="contact">
        <span class="contact-icon" aria-hidden="true">
          <svg viewBox="0 0 14 14"><rect x="1.5" y="3" width="11" height="8" fill="#fff"/><path d="M1.5 3l5.5 4.5L12.5 3" fill="none" stroke="var(--teal)" stroke-width="1"/></svg>
        </span>
        <p class="contact-text">info@holvaster-example.com<br>www.holvaster-example.com</p>
      </div>
    </div>
  </section>

</main>
</body>
</html>
```